Wedding Photo Studio needs custom webpage

I'm changing up my service offering to offer multiple editing styles. I'm looking to update my website to reflect that but still showcase my dreamy edits as an attention grabbing part of the website.

I will have 4 color editing styles (Lucian's Hallmark, Bright & Airy, Velvet Umber, Dreamy) and one black and white style. I have attached sample images in each style.

I also attached a couple dreamy edits that can be used as attention grabbing images.

I'm hoping for some functionality that perhaps takes a single image and divides it by 4 to show 25% in each style that can be clicked on and would 'maximize' the carousel to that style but still have a functionality to go to a different style after being maximized.

You can see www.lucianvphotography-demo.com for the current design and content. It doesn't have to be too different (but can be). It just needs to showcase the multiple editing styles effectively.

Target Market(s)

Couples who are having $20-50k weddings.

Industry/Entity Type

Photography

Coding

Coded - Design and coding required

Number of Pages Required

3 page

Colors

Designer to choose colors to be used in the design.

Requirements
Must have
• Pricing page with toggles for (off-season/on-season, Saturday/non-saturday) accurate pricing, good way to show multiple editing style photos.

```html
<!DOCTYPE html>
<html lang="en">
<head>
<meta charset="utf-8">
<title>Lucian V Photography — Kitchener-Waterloo Wedding Photographer</title>
<link rel="stylesheet" href="https://fonts.googleapis.com/css2?family=Montserrat:ital,wght@0,400;0,500;0,600;0,700;1,400;1,600&display=swap">
<style>
:root{
  --ink:#1b1b1b;
  --text:#3a3a3a;
  --gold:#c28f37;
  --gold-dark:#b5832d;
  --beige:#ede2cc;
  --paper:#faf8f4;
  --mist:#c9d9e6;
  --night:#0e0e0f;
  --white:#ffffff;
}
*{margin:0;padding:0;box-sizing:border-box}
html,body{width:1200px;height:3273px;overflow:hidden}
body{
  position:relative;
  font-family:'Montserrat',sans-serif;
  color:var(--text);
  background:
    radial-gradient(ellipse 420px 520px at 1200px 900px,rgba(180,204,224,.75),transparent 70%),
    radial-gradient(ellipse 380px 420px at 1160px 700px,rgba(190,210,228,.6),transparent 70%),
    radial-gradient(ellipse 420px 380px at 60px 2080px,rgba(190,210,228,.7),transparent 70%),
    radial-gradient(ellipse 380px 460px at 1200px 2300px,rgba(190,210,228,.7),transparent 70%),
    radial-gradient(ellipse 360px 300px at 380px 2060px,rgba(196,214,230,.55),transparent 70%),
    var(--paper);
}
.abs{position:absolute}

/* Hero */
.hero{position:absolute;left:0;top:0;width:1200px;height:625px;overflow:hidden}
.hero-photo{position:absolute;inset:0;
  background:
    radial-gradient(ellipse 500px 260px at 600px 560px,rgba(150,120,110,.55),transparent 70%),
    radial-gradient(ellipse 380px 300px at 880px 260px,rgba(196,110,50,.7),transparent 70%),
    radial-gradient(ellipse 320px 320px at 220px 330px,rgba(170,60,40,.65),transparent 70%),
    linear-gradient(180deg,#141828 0%,#2a2030 30%,#5a3320 62%,#3a2a28 100%);}
.main-nav{position:absolute;top:56px;left:0;width:1200px;display:flex;justify-content:center;gap:0}
.main-nav a{color:var(--white);text-decoration:none;font-size:10.5px;font-weight:600;letter-spacing:.2px;text-transform:uppercase;padding:0 12px}
.main-nav a.active{font-weight:700}
.hero-brand{position:absolute;top:146px;left:0;width:1200px;text-align:center;color:var(--white);font-size:26px;font-weight:500;letter-spacing:1px}
.hero-title{position:absolute;top:224px;left:0;width:1200px;text-align:center;color:var(--white);font-size:27px;font-weight:700;line-height:35px;text-transform:uppercase}
.hero-sub{position:absolute;top:304px;left:0;width:1200px;text-align:center;color:var(--white);font-size:13px;font-weight:700;text-transform:uppercase}
.hero-cities{position:absolute;top:332px;left:350px;width:500px;text-align:center;color:var(--white);font-size:14.5px;line-height:21px}
.hero-arrow{position:absolute;left:592px;top:552px}

/* Section headings */
.section-title{position:absolute;left:0;width:1200px;text-align:center;color:var(--ink);font-size:36px;font-weight:700;text-transform:uppercase}
.rule{position:absolute;height:2px;width:84px;background:var(--gold)}

/* Style showcase */
.style-grid{position:absolute;left:206px;top:849px;width:788px;height:528px;border:2px solid var(--gold);display:grid;grid-template-columns:1fr 1fr;grid-template-rows:266px 1fr;box-shadow:0 10px 18px rgba(0,0,0,.18)}
.style-tile{border:1px solid var(--gold)}
.tile-hallmark{background:linear-gradient(160deg,#b58a5a,#6d5a48 55%,#3e3a33)}
.tile-umber{background:linear-gradient(160deg,#7a3f25,#5a3a26 55%,#3a2e22)}
.tile-bw{background:linear-gradient(160deg,#9a9a9a,#5a5a5a 55%,#2e2e2e)}
.tile-airy{background:linear-gradient(160deg,#c8bfae,#b9b19a 55%,#6f7a4e)}
.style-label{position:absolute;left:164px;top:1190px;transform-origin:left top;transform:rotate(-90deg);font-size:14px;color:var(--ink);white-space:nowrap}

/* About */
.about-backdrop{position:absolute;left:236px;top:1825px;width:341px;height:275px;background:var(--beige)}
.about-photo{position:absolute;left:100px;top:1543px;width:443px;height:530px;background:linear-gradient(150deg,#6b4a3a,#9b5a3e 40%,#e7dcd4 70%,#8a6a52)}
.about-title{position:absolute;left:674px;top:1600px;font-size:36px;font-weight:700;color:var(--ink);text-transform:uppercase}
.signature{position:absolute;left:676px;top:1693px;width:150px;height:42px;background:linear-gradient(90deg,rgba(27,27,27,.12),rgba(27,27,27,.05))}
.about-copy{position:absolute;left:673px;top:1763px;width:428px;font-size:13.6px;line-height:22.5px;color:var(--text)}
.btn{position:absolute;left:673px;top:1980px;width:148px;height:38px;background:var(--gold);color:var(--white);font-size:13px;font-weight:700;text-transform:uppercase;display:flex;align-items:center;justify-content:center;box-shadow:0 4px 8px rgba(0,0,0,.15)}

/* Testimonials */
.stars{position:absolute;left:104px;top:2434px;display:flex;gap:3px}
.quote-mark{position:absolute;left:492px;top:2410px;font-size:120px;line-height:1;color:var(--beige);font-weight:700}
.client{position:absolute;left:103px;top:2484px;font-size:15px;color:var(--ink)}
.quote{position:absolute;left:104px;top:2516px;width:440px;font-size:13.6px;line-height:22.5px;font-style:italic;color:var(--text)}
.quote strong{color:var(--ink);font-weight:600}
.slide-arrows{position:absolute;left:103px;top:2642px;display:flex;gap:12px}
.testi-backdrop{position:absolute;left:612px;top:2472px;width:290px;height:236px;background:var(--beige)}
.testi-photo{position:absolute;left:641px;top:2365px;width:458px;height:315px;background:linear-gradient(180deg,#4a4a78 0%,#c96a6a 35%,#8a4a32 60%,#6a7a2a 85%,#3a3a40)}

/* Footer */
.site-footer{position:absolute;left:0;top:2794px;width:1200px;height:479px;background:var(--night);color:var(--white)}
.footer-brand{position:absolute;top:100px;left:0;width:1200px;text-align:center;font-size:26px;font-weight:500;letter-spacing:1px}
.footer-nav{position:absolute;top:188px;left:0;width:1200px;display:flex;justify-content:center;gap:32px}
.footer-nav a{color:var(--white);text-decoration:none;font-size:14.5px;font-weight:500;text-transform:uppercase}
.footer-nav a.active{font-weight:700}
.footer-rule{position:absolute;left:108px;width:982px;height:1px;background:#2e2e2e}
.contact{position:absolute;top:284px;display:flex;gap:12px}
.contact h4{font-size:16px;font-weight:400;text-transform:uppercase;margin-bottom:6px}
.contact p{font-size:15px;line-height:25px}
.copyright{position:absolute;top:418px;left:0;width:1200px;text-align:center;font-size:14px}
</style>
</head>
<body>

<header class="hero">
  <div class="hero-photo" role="img" aria-label="Night photo of a couple dancing in front of a lit modern venue entrance under a starry sky"></div>
  <nav class="main-nav">
    <a class="active" href="#">Home</a><a href="#">The Team</a><a href="#">Portfolio</a><a href="#">Blog</a><a href="#">Pricing</a><a href="#">Contact Me</a>
  </nav>
  <div class="hero-brand">Lucian V Photography</div>
  <h1 class="hero-title">Kitchener-Waterloo Wedding<br>Photographer</h1>
  <p class="hero-sub">Also Serving</p>
  <p class="hero-cities">Toronto, Hamilton, London, Niagara, Cambridge, Mississauga, Brampton, Burlington, Guelph</p>
  <svg class="hero-arrow" width="16" height="36" viewBox="0 0 16 36" fill="none" stroke="#fff" stroke-width="1.4"><path d="M8 2v32M2 27l6 7 6-7"/></svg>
</header>

<h2 class="section-title" style="top:738px">The Lucian V Style</h2>
<div class="rule" style="left:558px;top:795px"></div>

<div class="style-grid">
  <div class="style-tile tile-hallmark" role="img" aria-label="Wedding couple by a waterfall in the Lucian's Hallmark edit"></div>
  <div class="style-tile tile-umber" role="img" aria-label="Wedding couple by a waterfall in the Velvet Umber edit"></div>
  <div class="style-tile tile-bw" role="img" aria-label="Wedding couple by a waterfall in the black and white edit"></div>
  <div class="style-tile tile-airy" role="img" aria-label="Wedding couple by a waterfall in the Bright &amp; Airy edit"></div>
</div>
<div class="style-label">Black and White</div>
<svg class="abs" style="left:172px;top:1312px" width="28" height="18" viewBox="0 0 28 18" fill="none" stroke="#c28f37" stroke-width="1.3"><path d="M26 14C18 15 10 12 4 4M4 4l0 7M4 4l7 1"/></svg>

<div class="about-backdrop"></div>
<div class="about-photo" role="img" aria-label="Bride and groom on stone steps beside autumn red foliage"></div>
<h2 class="about-title">About Me</h2>
<div class="rule" style="left:674px;top:1655px"></div>
<div class="signature" role="img" aria-label="Handwritten signature of Lucian Varga"></div>
<p class="about-copy">I am an accountant by day, photographer by night. I once read a happy life is had by loving your job, loving your creative hobby and the love of family; photography is one part of that for me. I focus primarily on wedding photography in southern Ontario. I cover Toronto, Hamilton, Kitchener, Waterloo, London and anywhere in the world you want to send me. If you like what I do, please reach out; I'm happy to meet with you and chat more about your big day.</p>
<a class="btn">Learn More</a>

<h2 class="section-title" style="top:2222px">Client Testimonials</h2>
<div class="rule" style="left:558px;top:2274px"></div>

<div class="stars">
  <svg width="89" height="17" viewBox="0 0 89 17" fill="#c28f37">
    <path id="star" d="M8.5 0l2.5 5.6 6 .6-4.5 4 1.3 6-5.3-3.1-5.3 3.1 1.3-6L0 6.2l6-.6z"/>
    <use href="#star" x="18"/><use href="#star" x="36"/><use href="#star" x="54"/><use href="#star" x="72"/>
  </svg>
</div>
<div class="quote-mark">&rdquo;</div>
<p class="client">Mark &amp; Elena</p>
<p class="quote">Lucian did an outstanding job on our wedding photos! We got so so much more for so so much less. Thanks again Lucian, you exceeded our expectations and then some.<br><strong>I recommend him 100 times over!</strong></p>
<div class="slide-arrows">
  <svg width="18" height="12" viewBox="0 0 18 12" fill="none" stroke="#c28f37" stroke-width="1.4"><path d="M17 6H2M6 1L1 6l5 5"/></svg>
  <svg width="18" height="12" viewBox="0 0 18 12" fill="none" stroke="#c28f37" stroke-width="1.4"><path d="M1 6h15M12 1l5 5-5 5"/></svg>
</div>
<div class="testi-backdrop"></div>
<div class="testi-photo" role="img" aria-label="Couple in front of a brick heritage building at sunset with a reflecting pool"></div>

<footer class="site-footer">
  <div class="footer-brand">Lucian V Photography</div>
  <nav class="footer-nav">
    <a class="active" href="#">Home</a><a href="#">The Team</a><a href="#">Portfolio</a><a href="#">Blog</a><a href="#">Pricing</a><a href="#">Contact Me</a>
  </nav>
  <div class="footer-rule" style="top:244px"></div>

  <div class="contact" style="left:108px">
    <svg width="18" height="22" viewBox="0 0 18 22" fill="none" stroke="#fff" stroke-width="1.3"><path d="M9 21s7-7 7-12A7 7 0 0 0 2 9c0 5 7 12 7 12z"/><circle cx="9" cy="9" r="2.5"/></svg>
    <div><h4>Address</h4><p>Kitchener, ON, Canada,<br>Ontario</p></div>
  </div>
  <div class="contact" style="left:363px">
    <svg width="24" height="18" viewBox="0 0 24 18" fill="none" stroke="#fff" stroke-width="1.3"><rect x="1" y="1" width="22" height="16" rx="1"/><path d="M1 2l11 8 11-8"/></svg>
    <div><h4>Email</h4><p>lucian@lucianvphotography-demo.com</p></div>
  </div>
  <div class="contact" style="left:685px">
    <svg width="22" height="22" viewBox="0 0 22 22" fill="none" stroke="#fff" stroke-width="1.3"><path d="M5 2l4 4-2 3c1 3 3 5 6 6l3-2 4 4-3 3C9 20 2 13 2 5z"/></svg>
    <div><h4>Phone</h4><p>+1 555-010-2847</p></div>
  </div>
  <div class="contact" style="left:885px">
    <svg width="22" height="22" viewBox="0 0 22 22" fill="none" stroke="#fff" stroke-width="1.5"><circle cx="11" cy="11" r="9.5"/><path d="M11 5v6h-4"/></svg>
    <div><h4>Hours</h4><p>Mon to Fri: 9am - 5pm<br>Sat &amp; Sun: Closed</p></div>
  </div>

  <div class="footer-rule" style="top:389px"></div>
  <p class="copyright">2025 Lucian V Photography. All Rights Reserved</p>
</footer>

</body>
</html>
```